50th Anniversary Gala Save the date Postcard 8.5x5.5 inches

Looking for a 5.5x8.5 in one-sided postcard design for our annual gala. Design needs to include "Save the date" prominently with all the event information included below. Design should be light, include the colors of our logo and elegant. (almost like a wedding save the date). "Threads of Grace" should look like its own logo.

50th Anniversary Gala at The Lodge at Fernwick Glen – “Threads of Grace – Celebrating 50 Years of Building Community”
Thursday, October 24
6-11p
The Lodge at Fernwick Glen
Marlowe Parkway, Alderbrook Springs, VT
Honoring – TBW Previous Presidents

Target Market(s)

Exisiting donors

Industry/Entity Type

nonprofit

Font styles to use
Serif
Script

Requirements
Must have
• Save the date prominent
Should not have
• should not have a dark background

```html
<!DOCTYPE html>
<html lang="en">
<head>
<meta charset="utf-8">
<title>Save The Date – 50th Anniversary Gala</title>
<link href="https://fonts.googleapis.com/css2?family=Dancing+Script:wght@700&family=Marcellus&family=Lora:ital,wght@1,400;1,700&display=swap" rel="stylesheet">
<style>
  :root {
    --page: #ededed;
    --card: #ffffff;
    --gold: #d79d12;
    --gold-line: #d4a44a;
    --navy: #173d78;
    --sky: #1a8ed3;
    --blush: #ecd2c0;
    --sand: #d9bfa2;
    --rose: #f0c8be;
  }
  * { margin: 0; padding: 0; box-sizing: border-box; }
  html, body { width: 1200px; height: 910px; overflow: hidden; background: var(--page); }
  .postcard {
    position: absolute; left: 0; top: 67px;
    width: 1200px; height: 776px;
    background: var(--card);
    overflow: hidden;
    font-family: "Marcellus", "Times New Roman", serif;
    color: var(--navy);
  }
  .frame-line { position: absolute; }
  .frame-top { left: 28px; top: 25px; width: 822px; height: 2px;
    background: linear-gradient(90deg, #e2c27a, var(--gold-line) 60%, #c99a3c); }
  .frame-left { left: 28px; top: 25px; width: 2px; height: 538px;
    background: linear-gradient(180deg, var(--gold-line), #f3e3b8 70%, rgba(243,227,184,0)); }
  .frame-right { left: 1170px; top: 194px; width: 2px; height: 556px;
    background: linear-gradient(180deg, #e6cd92, var(--gold-line)); }
  .frame-bottom { left: 205px; top: 748px; width: 967px; height: 2px;
    background: linear-gradient(90deg, rgba(212,164,74,0), var(--gold-line) 15%, #c99a3c); }

  .floral { position: absolute; }
  .floral-top-right { left: 900px; top: -40px; width: 340px; height: 300px;
    background: radial-gradient(closest-side at 62% 40%, var(--rose) 0%, var(--blush) 35%, var(--sand) 60%, rgba(255,255,255,0) 100%); }
  .floral-bottom-left { left: -60px; top: 450px; width: 290px; height: 380px;
    background: radial-gradient(closest-side at 40% 62%, var(--rose) 0%, var(--sand) 45%, var(--blush) 70%, rgba(255,255,255,0) 100%); }

  .brand { position: absolute; left: 90px; top: 78px; width: 220px;
    display: flex; align-items: center; gap: 10px; }
  .brand-dot { width: 14px; height: 14px; border-radius: 50%; background: var(--sky); flex: none; }
  .brand-name { font-size: 34px; line-height: 1.02; color: var(--sky); }

  .tagline { position: absolute; left: 330px; top: 108px; width: 540px; text-align: center;
    font-family: "Lora", Georgia, serif; font-style: italic; font-size: 24px; color: var(--navy); white-space: nowrap; }
  .tagline strong { font-weight: 700; }

  .headline { position: absolute; left: 0; top: 195px; width: 1200px; text-align: center;
    font-family: "Dancing Script", cursive; font-weight: 700; font-size: 150px; line-height: 1;
    color: var(--gold); white-space: nowrap; }

  .date-row { position: absolute; left: 271px; top: 397px; width: 658px; height: 62px; }
  .date-side { position: absolute; top: 0; width: 258px; height: 61px;
    border-top: 1.5px solid var(--navy); border-bottom: 1.5px solid var(--navy);
    display: flex; align-items: center; justify-content: center;
    font-size: 37px; letter-spacing: 4px; color: var(--navy); -webkit-text-stroke: 0.8px var(--navy); }
  .date-month { left: 0; }
  .date-weekday { right: 0; }
  .date-day { position: absolute; left: 258px; width: 142px; top: -14px; text-align: center;
    font-size: 84px; line-height: 1; color: var(--sky); letter-spacing: 4px; -webkit-text-stroke: 1.5px var(--sky); }

  .time { position: absolute; left: 0; top: 484px; width: 1200px; text-align: center;
    font-size: 33px; letter-spacing: 3px; color: var(--navy); -webkit-text-stroke: 0.7px var(--navy); }
  .venue { position: absolute; left: 0; top: 566px; width: 1200px; text-align: center;
    font-size: 26px; line-height: 36px; letter-spacing: 1.5px; color: var(--navy); }
  .honoree { position: absolute; left: 0; top: 678px; width: 1200px; text-align: center;
    font-size: 16px; letter-spacing: 2.5px; color: var(--navy); }
</style>
</head>
<body>
  <main class="postcard">
    <div class="frame-line frame-top"></div>
    <div class="frame-line frame-left"></div>
    <div class="frame-line frame-right"></div>
    <div class="frame-line frame-bottom"></div>

    <div class="floral floral-top-right" role="img" aria-label="Dried palm fans, pampas grass and blush roses in the corner"></div>
    <div class="floral floral-bottom-left" role="img" aria-label="Dried palm fans, pampas grass and blush berries in the corner"></div>

    <div class="brand">
      <span class="brand-dot"></span>
      <span class="brand-name">Threads<br>of Grace</span>
    </div>

    <p class="tagline">Celebrating <strong>50 Years</strong> of Building Community</p>

    <h1 class="headline">Save The Date</h1>

    <div class="date-row">
      <div class="date-side date-month">OCTOBER</div>
      <div class="date-day">24</div>
      <div class="date-side date-weekday">THURSDAY</div>
    </div>

    <p class="time">6.00PM - 11.00PM</p>

    <p class="venue">THE LODGE AT FERNWICK GLEN<br>MARLOWE PARKWAY, ALDERBROOK SPRINGS, VT</p>

    <p class="honoree">HONORING TBW PREVIOUS PRESIDENTS</p>
  </main>
</body>
</html>
```